Flyer needed to promote gutter clearance service for established gardening company

We need a bright and engaging flyer to be designed to advertise our gutter clearance service.
Whilst we are a gardening company that normally does more horticultural work, during the winter we offer other services such as gutter clearance where we remove the debris from gutters and thereby reducing the risk of clogs, leakage, breakage and potential structural damage to the property.

Full details of our service, together with our overall brand and colours can be seen on www.marlowtreecare.co.uk/gutters.

We would like you to use the page on the website as a basis to create the flyer and so please feel free to use as much or as little of the wording contained within the webpage on the flyer drawing particular attention to "Prices starting at just £60 for an average 3 bed house". I will upload pictures but please feel free to use other graphics and fonts to make it stand out.

The contact details which should be included within the flyer are as follows:

Marlow Treecare Services Ltd
Orbit Trading Centre
Fairbrook Vale Ind Estate
Swindon
SN4 7HW

Tel: 01793 418302
www.marlowtreecare.co.uk
dean@marlowtreecare.co.uk

The flyers will eventually be printed out in A5 (210mm x 148mm) using Printelle and so needs to be in that size and suitable file for upload.

I have only put this as a 2 day project as its really urgent and I'm hoping we get some great designs in that time.

Target Market(s)

Homeowners between 25 - 65+

Industry/Entity Type

Home Improvement

Font styles to use
Serif
Sans Serif
Decorative
Script

Colors
6b449b
9bcb3c

Requirements
Must have
• Our colours are purple and green as seen on our website www.marlowtreecare.co.uk/gutters. Please use those colours.
• The flyer should draw attention to the following facts:
• We are Marlow Treecare Services Ltd (see attached logo)
• We are offering a Gutter Clearance Service in Swindon
• Prices start at just £60 for the average 3 bed house.
• We are fully insured.
• Our contact details must be included (as in the product description above)
• I have attached pictures but feel free to add other graphics or use fonts to make the flyer more engaging and interesting.
• Additional wording may be taken from the website at the address shown above. You can use as much or as little wording as you like just as long as the message gets across and the flyer contains our contact information and logo and the details shown above.
Nice to have
• I would like a bright and modern design which isn't too busy or cluttered. It should be something that is quick and easy to read.
Should not have
• I don't want it to look too busy or crowded with small type which people just won't read. Whilst I've said you can take whatever wording you want from our website, I'd suggest you don't take it all or too much. I want the main message (as detailed above in 'must haves') to stand out rather than have it contained deep within lots of small type face.

```html
<!DOCTYPE html>
<html lang="en">
<head>
<meta charset="utf-8">
<title>Marlow Treecare Services – Gutter Clearance Flyer</title>
<link href="https://fonts.googleapis.com/css2?family=Arimo:wght@400;700&family=PT+Sans+Narrow&display=swap" rel="stylesheet">
<style>
  :root {
    --purple: #6b449b;
    --green: #9bcb3c;
    --white: #ffffff;
    --ink: #1c1c1c;
    --brand-ink: #3b2516;
  }
  * { box-sizing: border-box; margin: 0; padding: 0; }
  html, body { width: 852px; height: 1200px; overflow: hidden; background: var(--white); }
  body { font-family: "Arimo", Arial, sans-serif; }
  .flyer { position: relative; width: 852px; height: 1200px; overflow: hidden; background: var(--white); }

  .top-wave { position: absolute; left: 0; top: 0; width: 852px; height: 130px; }

  .brand { position: absolute; left: 50px; top: 110px; display: flex; align-items: center; gap: 14px; }
  .brand-dot { width: 34px; height: 34px; border-radius: 50%; background: var(--green); flex: none; }
  .brand-name { color: var(--brand-ink); font-weight: 400; line-height: 1; }
  .brand-name .main { display: block; font-size: 62px; letter-spacing: -1px; }
  .brand-name .sub { display: block; font-size: 17px; letter-spacing: 3.5px; margin-top: 8px; text-transform: uppercase; }

  .insured-badge {
    position: absolute; left: 559px; top: 54px; width: 212px; height: 212px; border-radius: 50%;
    background: var(--purple); color: var(--white);
    display: flex; flex-direction: column; align-items: center; justify-content: center;
    font-variant: small-caps; font-weight: 700; font-size: 30px; line-height: 1.25; text-align: center;
  }

  .services-title {
    position: absolute; left: 76px; top: 252px; color: var(--purple);
    font-variant: small-caps; font-weight: 700; font-size: 32px; letter-spacing: 0.3px;
  }
  .service { position: absolute; color: var(--purple); font-size: 22px; display: flex; align-items: center; gap: 14px; }
  .service::before { content: ""; width: 14px; height: 14px; border-radius: 50%; background: var(--purple); }

  .photo { position: absolute; }
  .photo-garden { left: 11px; top: 446px; width: 400px; height: 261px;
    background: linear-gradient(180deg, #3f6e2c 0%, #6e9a3a 30%, #d9913a 52%, #7b6fb8 62%, #7fa84a 75%, #8cb24f 100%); }
  .photo-gutter { left: 429px; top: 446px; width: 408px; height: 260px;
    background: linear-gradient(135deg, #9aa84a 0%, #4a4d52 35%, #3b3e44 60%, #d9a94a 85%, #c78a35 100%); }

  .promo-band { position: absolute; left: 0; top: 718px; width: 850px; height: 384px;
    background: radial-gradient(ellipse at 62% 55%, #8b4fa8 0%, #7a4b93 30%, #6d9a3f 65%, #8cbf4a 100%); }
  .price-line { position: absolute; left: 50px; top: 724px; font-family: "PT Sans Narrow", "Arial Narrow", sans-serif;
    font-size: 27px; color: var(--ink); letter-spacing: 0.2px; }
  .address { position: absolute; left: 35px; top: 924px; color: var(--white); font-size: 23px; line-height: 27.5px; font-style: normal; }
  .offer-line { position: absolute; left: 227px; top: 1062px; color: var(--ink); font-size: 21px; }

  .footer { position: absolute; left: 0; top: 1114px; width: 852px; height: 86px; background: var(--green); }
  .contact { position: absolute; top: 1150px; color: var(--white); font-size: 18.5px; display: flex; align-items: center; gap: 6px; }
  .contact svg { flex: none; }
</style>
</head>
<body>
<div class="flyer">
  <svg class="top-wave" viewBox="0 0 852 130" aria-hidden="true">
    <path d="M0 0 H852 V92 C760 105 700 125 600 118 C460 108 300 50 150 52 C80 53 30 60 0 66 Z" fill="var(--green)"/>
  </svg>

  <div class="brand">
    <span class="brand-dot"></span>
    <span class="brand-name"><span class="main">Marlow</span><span class="sub">Treecare Services</span></span>
  </div>

  <div class="insured-badge"><span>We are</span><span>fully</span><span>insured</span></div>

  <h2 class="services-title">Our Gardening Services</h2>
  <div class="service" style="left:64px;top:308px;">Mowing</div>
  <div class="service" style="left:310px;top:306px;">Weeding</div>
  <div class="service" style="left:602px;top:306px;">Landscaping</div>
  <div class="service" style="left:64px;top:365px;">Pruning</div>
  <div class="service" style="left:288px;top:364px;">Planting &amp; design</div>
  <div class="service" style="left:588px;top:364px;">Hedge trimming</div>

  <div class="photo photo-garden" role="img" aria-label="Colourful flower border beside a green lawn"></div>
  <div class="photo photo-gutter" role="img" aria-label="Gloved hands clearing autumn leaves from a roof gutter"></div>

  <div class="promo-band" role="img" aria-label="Close-up of purple allium flower heads"></div>
  <p class="price-line">PRICES START AT JUST £60 FOR THE AVERAGE 3 BED HOUSE</p>
  <address class="address">
    Marlow Treecare Services Ltd<br>
    Orbit Trading Centre<br>
    Fairbrook Vale Ind Estate<br>
    Swindon<br>
    SN4 7HW
  </address>
  <p class="offer-line">We are offering a Gutter Clearance Service in Swindon</p>

  <div class="footer"></div>
  <div class="contact" style="left:34px;">
    <svg width="16" height="16" viewBox="0 0 24 24" aria-hidden="true"><path fill="#fff" d="M6.6 10.8a15 15 0 0 0 6.6 6.6l2.2-2.2c.3-.3.7-.4 1-.2 1.1.4 2.3.6 3.6.6.6 0 1 .4 1 1V20c0 .6-.4 1-1 1A17 17 0 0 1 3 4c0-.6.4-1 1-1h3.5c.6 0 1 .4 1 1 0 1.3.2 2.5.6 3.6.1.3 0 .7-.2 1z"/></svg>
    <span>01793 418302</span>
  </div>
  <div class="contact" style="left:218px;">
    <svg width="18" height="14" viewBox="0 0 18 14" aria-hidden="true"><rect x="1" y="1" width="16" height="12" fill="none" stroke="#fff" stroke-width="1.3"/><path d="M1 1 L9 8 L17 1 M1 13 L7 6.5 M17 13 L11 6.5" fill="none" stroke="#fff" stroke-width="1.3"/></svg>
    <span style="margin-left:12px;">www.marlowtreecare.co.uk</span>
  </div>
  <div class="contact" style="left:532px;">
    <svg width="14" height="14" viewBox="0 0 14 14" aria-hidden="true"><circle cx="7" cy="7" r="6" fill="none" stroke="#fff" stroke-width="1.1"/><ellipse cx="7" cy="7" rx="2.6" ry="6" fill="none" stroke="#fff" stroke-width="1"/><path d="M1 7 H13 M2 4 H12 M2 10 H12" stroke="#fff" stroke-width="1"/></svg>
    <span>dean@marlowtreecare.co.uk</span>
  </div>
</div>
</body>
</html>
```